Property inspection company needs logo/business card design

A new, home, commercial, and multi dwelling inspection company needs help with a new logo and hence business cards.

Time is extended for the rest of the week.

Font styles to use
Sans Serif

Colors
ec1f27
0255a3
ffffff

```html
<!DOCTYPE html>
<html lang="en">
<head>
<meta charset="utf-8">
<title>Halden Ridge Inspections – Business Card</title>
<link href="https://fonts.googleapis.com/css2?family=Oswald:wght@500&family=Lato:wght@400&display=swap" rel="stylesheet">
<style>
  :root {
    --stage: #2a2a2a;
    --card-white: #ffffff;
    --brand-red: #a81e25;
    --accent-red: #b3212a;
    --ink: #1e1e1e;
    --rule: #d4d4d4;
    --on-red: #ffffff;
  }
  html, body {
    margin: 0;
    padding: 0;
    width: 1200px;
    height: 900px;
    overflow: hidden;
    background: var(--stage);
  }
  .canvas {
    position: relative;
    width: 1200px;
    height: 900px;
  }
  .card {
    position: absolute;
    width: 477px;
    height: 294px;
    box-shadow: 3px 4px 6px rgba(0,0,0,0.45);
  }
  .card-front {
    left: 120px;
    top: 275px;
    background: var(--card-white);
    border-radius: 0 46px 0 46px;
  }
  .card-back {
    left: 606px;
    top: 273px;
    background: var(--brand-red);
    border-radius: 46px 0 46px 0;
  }
  .brand-block {
    position: absolute;
    left: 40px;
    top: 92px;
    width: 190px;
    text-align: center;
  }
  .brand-square {
    display: block;
    width: 26px;
    height: 26px;
    margin: 0 auto 14px;
    background: var(--accent-red);
  }
  .brand-name {
    font-family: 'Oswald', sans-serif;
    font-weight: 500;
    font-size: 23px;
    line-height: 1.1;
    color: var(--accent-red);
    letter-spacing: 0.5px;
    margin: 0;
  }
  .divider {
    position: absolute;
    left: 239px;
    top: 73px;
    width: 1px;
    height: 146px;
    background: var(--rule);
  }
  .contact-block {
    position: absolute;
    left: 262px;
    top: 66px;
    font-family: 'Lato', sans-serif;
    color: var(--ink);
  }
  .person-name {
    font-family: 'Oswald', sans-serif;
    font-weight: 500;
    font-size: 19px;
    line-height: 1;
    color: var(--accent-red);
    margin: 0;
    letter-spacing: 0.2px;
  }
  .person-role {
    font-size: 13.5px;
    margin: 3px 0 7px;
  }
  .contact-list {
    list-style: none;
    margin: 0;
    padding: 0;
  }
  .contact-item {
    display: flex;
    align-items: center;
    font-size: 14px;
    line-height: 17.5px;
  }
  .contact-icon {
    width: 10px;
    height: 10px;
    margin-right: 4px;
    fill: var(--accent-red);
  }
  .address {
    font-size: 14px;
    line-height: 17.5px;
    margin: 6px 0 0;
    font-style: normal;
  }
  .back-brand {
    position: absolute;
    left: 0;
    right: 0;
    top: 100px;
    text-align: center;
  }
  .back-square {
    display: block;
    width: 34px;
    height: 34px;
    margin: 0 auto 16px;
    background: var(--on-red);
  }
  .back-name {
    font-family: 'Oswald', sans-serif;
    font-weight: 500;
    font-size: 30px;
    line-height: 1;
    color: var(--on-red);
    letter-spacing: 1px;
    margin: 0;
  }
</style>
</head>
<body>
<main class="canvas">
  <section class="card card-front">
    <div class="brand-block">
      <span class="brand-square"></span>
      <p class="brand-name">HALDEN RIDGE<br>INSPECTIONS</p>
    </div>
    <div class="divider"></div>
    <div class="contact-block">
      <h1 class="person-name">DANIEL CARTER</h1>
      <p class="person-role">Managing Director</p>
      <ul class="contact-list">
        <li class="contact-item">
          <svg class="contact-icon" viewBox="0 0 10 10"><path d="M1 3.5C1 2 3 1.5 5 1.5S9 2 9 3.5v1H7V3.6H3v.9H1z"/><rect x="2" y="5" width="6" height="4" rx="1"/></svg>
          044-123 456 789
        </li>
        <li class="contact-item">
          <svg class="contact-icon" viewBox="0 0 10 10"><path d="M3 0h4a1 1 0 0 1 1 1v8a1 1 0 0 1-1 1H3a1 1 0 0 1-1-1V1a1 1 0 0 1 1-1zm.5 1.2v6.6h3V1.2z"/></svg>
          044-123 456 789
        </li>
        <li class="contact-item">
          <svg class="contact-icon" viewBox="0 0 10 10"><path d="M0 2h10v.8L5 6 0 2.8z"/><path d="M0 3.8 5 7l5-3.2V8H0z"/></svg>
          info@webname.com
        </li>
        <li class="contact-item">
          <svg class="contact-icon" viewBox="0 0 10 10"><circle cx="5" cy="5" r="5"/></svg>
          www.websitename.com
        </li>
      </ul>
      <address class="address">12345, Address Goes Here<br>Country Name, 123456.</address>
    </div>
  </section>

  <section class="card card-back">
    <div class="back-brand">
      <span class="back-square"></span>
      <p class="back-name">HALDEN RIDGE INSPECTIONS</p>
    </div>
  </section>
</main>
</body>
</html>
```